Modern/Bold/Unique Prenatal Vitamin label redesign

We are in need of a design update for our Prenatal Vitamin label. We want to modernize our label and give it a fresh feel.
It should bring a feeling of fun, joy, and sophistication, but also be bold/edgy/unique and portray Trust and Authority. Our buyers are mainly mothers in the age range of 25-34 who are pregnant or breastfeeding.
I will attach our current label design, as well as some inspiration to go off of.
We like the idea of having a clean, easy to read label label with bold/vibrant colors and fonts. We like the idea of having some retro vibes in it as well
Please see the attached artwork for design inspiration (New Design Idea). We like the idea of having a pregnant mother image like the attachment on the label, with the rest of the label being white. Please come up with a unique drawing/image for the design. We cannot use a copied image or stock image.
We look forward to working with you!

```html
<!DOCTYPE html>
<html lang="en">
<head>
<meta charset="utf-8">
<title>Bloomwell Prenatal Glow – Label</title>
<link rel="stylesheet" href="https://fonts.googleapis.com/css2?family=Heebo:wght@300;500;700&family=Libre+Baskerville&display=swap">
<style>
  :root {
    --stage: #b3b3b3;
    --label-top: #e6c78f;
    --label-mid: #d3aaa6;
    --label-low: #caa0bc;
    --label-bottom: #c79bc9;
    --ink-light: #f4eeee;
    --figure-top: #8f3fbf;
    --figure-mid: #c640c2;
    --figure-low: #d96bcf;
  }
  * { margin: 0; padding: 0; box-sizing: border-box; }
  html, body {
    width: 1200px; height: 900px; overflow: hidden;
    background: var(--stage);
  }
  .canvas {
    position: relative; width: 1200px; height: 900px;
    display: flex; align-items: center; justify-content: center;
  }
  .label {
    position: relative; width: 660px; height: 840px; overflow: hidden;
    background: linear-gradient(180deg, var(--label-top) 0%, var(--label-mid) 45%, var(--label-low) 75%, var(--label-bottom) 100%);
    font-family: "Heebo", sans-serif; color: var(--ink-light);
  }
  .brand-name {
    position: absolute; top: 62px; left: 0; right: 0;
    text-align: center; font-weight: 500; font-size: 60px; letter-spacing: 0.5px;
  }
  .mother-illustration {
    position: absolute; left: 398px; top: 176px; width: 200px; height: 520px;
    border-radius: 90px 90px 40px 60px;
    background: linear-gradient(180deg, var(--figure-top) 0%, var(--figure-mid) 60%, var(--figure-low) 88%, rgba(217,107,207,0) 100%);
  }
  .product-name {
    position: absolute; left: 104px; top: 380px;
    font-family: "Libre Baskerville", serif; font-size: 84px; line-height: 1.05;
  }
  .product-name span { display: block; padding-left: 150px; }
  .tagline {
    position: absolute; left: 66px; top: 624px;
    font-weight: 300; font-size: 24px; line-height: 1.2;
  }
  .tagline strong { font-weight: 700; }
  .supplement-note {
    position: absolute; left: 62px; bottom: 28px;
    font-weight: 300; font-size: 25px;
  }
  .count-badge {
    position: absolute; right: 100px; bottom: 28px;
    display: flex; align-items: flex-start; gap: 6px;
  }
  .count-number { font-weight: 700; font-size: 44px; line-height: 1; }
  .count-unit { font-weight: 300; font-size: 14px; line-height: 1.05; text-align: center; }
</style>
</head>
<body>
<main class="canvas">
  <section class="label">
    <div class="brand-name">Bloomwell</div>

    <div class="mother-illustration" role="img" aria-label="Illustration of a pregnant mother in profile, silhouette in purple and magenta"></div>

    <h1 class="product-name">Prenatal<span>Glow</span></h1>

    <p class="tagline">Once Daily<br>Premium Multivitamin for<br><strong>Mama &amp; Baby *</strong></p>

    <p class="supplement-note">Dietary Supplement</p>

    <div class="count-badge">
      <svg width="34" height="72" viewBox="0 0 34 72" aria-hidden="true">
        <rect x="2" y="2" width="30" height="68" rx="15" fill="none" stroke="#f4eeee" stroke-width="3"/>
        <path d="M2 36 H32 V17 A15 15 0 0 0 2 17 Z" fill="#f4eeee" opacity="0.35"/>
        <line x1="2" y1="36" x2="32" y2="36" stroke="#f4eeee" stroke-width="3"/>
      </svg>
      <div>
        <div class="count-number">90</div>
        <div class="count-unit">Veggie<br>Capsules</div>
      </div>
    </div>
  </section>
</main>
</body>
</html>
```